BrightWay, LLC - Business consulting

Need a logo design for my new start-up consulting business. I provide consulting to both profit and non-profit organizations providing full-service strategic project management and organizational effectiveness consultation. The company name is BrightWay (with a capital D). I want my logo to represent the name as well as the services I provide.

Target Market(s)

C-level corporate and private foundation leaders

Industry/Entity Type

Business

Contact Information for Business Card

The Business Card will need to have contact details. I don't want much about the type of services - the logo should speak for itself. Preference for a vertical card - but not required. Contact info: Marla Trenholt, President, BrightWay LLC, 2450 Wren Lane, Cedarbrook MD 20999 240.555.3172 mtrenholt@brightwayadvise.example

Colors
876aae

Requirements
Must have
• clean look, professional and modern
Nice to have
• something with a "bulls-eye" to reflect the idea of focused, verical card

```html
<!DOCTYPE html>
<html lang="en">
<head>
<meta charset="utf-8">
<title>BrightWay, LLC — Business Card</title>
<link rel="stylesheet" href="https://fonts.googleapis.com/css2?family=Open+Sans:ital,wght@0,400;0,600;1,400&family=Tinos:ital@1&display=swap">
<style>
  :root {
    --page: #ffffff;
    --ink: #111111;
    --frame: #333333;
    --brand: #8b4fa6;
  }
  * { margin: 0; padding: 0; box-sizing: border-box; }
  html, body {
    width: 800px;
    height: 1200px;
    overflow: hidden;
    background: var(--page);
  }
  .canvas {
    position: relative;
    width: 800px;
    height: 1200px;
    background: var(--page);
  }
  .card {
    position: absolute;
    left: 207px;
    top: 300px;
    width: 402px;
    height: 598px;
    border: 1px solid var(--frame);
    background: var(--page);
    color: var(--ink);
    text-align: center;
    font-family: "Open Sans", Arial, sans-serif;
  }
  .card > * {
    position: absolute;
    left: 0;
    width: 100%;
  }
  .company-title {
    top: 32px;
    font-family: "Tinos", "Times New Roman", serif;
    font-style: italic;
    font-weight: 400;
    font-size: 57px;
    line-height: 1.2;
    letter-spacing: -0.5px;
    white-space: nowrap;
  }
  .brand-mark {
    top: 122px;
    height: 196px;
    display: flex;
    align-items: center;
    justify-content: center;
    gap: 14px;
  }
  .brand-mark__dot {
    width: 40px;
    height: 40px;
    border-radius: 50%;
    background: var(--brand);
  }
  .brand-mark__name {
    font-weight: 600;
    font-size: 40px;
    color: var(--brand);
  }
  .person-name {
    top: 345px;
    font-size: 32px;
    line-height: 1.3;
  }
  .person-role {
    top: 384px;
    font-size: 25px;
    line-height: 1.3;
  }
  .divider {
    top: 431px;
    left: 78px;
    width: 243px;
    height: 0;
    border-top: 1.5px solid var(--ink);
  }
  .contact {
    top: 445px;
    font-size: 21px;
    line-height: 30px;
    font-style: normal;
  }
  .contact__email {
    display: block;
    font-style: italic;
    font-size: 19.5px;
    margin-top: 2px;
    white-space: nowrap;
  }
</style>
</head>
<body>
  <main class="canvas">
    <section class="card">
      <h1 class="company-title">BrightWay, LLC</h1>
      <div class="brand-mark">
        <span class="brand-mark__dot" aria-hidden="true"></span>
        <span class="brand-mark__name">BrightWay</span>
      </div>
      <p class="person-name">Marla Trenholt</p>
      <p class="person-role">President</p>
      <hr class="divider">
      <address class="contact">
        2450 Wren Lane,<br>
        Cedarbrook MD 20999<br>
        240.555.3172
        <span class="contact__email">mtrenholt@brightwayadvise.example</span>
      </address>
    </section>
  </main>
</body>
</html>
```